Fundraising Study Day East of England. Lift the January blues!

A flyer to advertise a fundraising event of lectures for dental hygienists and therapists in support of the exemption campaign. Currently dental hygienists and therapists require a prescription to deliver certain treatment or recommend certain toothpastes. If we are successful in the campaign we will be able to treat patients without these restrictions.

Dental

```html
<!DOCTYPE html>
<html lang="en">
<head>
<meta charset="utf-8">
<title>Fundraising Study Day East of England</title>
<link href="https://fonts.googleapis.com/css2?family=PT+Sans:ital,wght@0,700;1,700&family=Montserrat:wght@500;600&family=Open+Sans:ital,wght@0,400;0,600;1,600;1,700&family=Roboto+Condensed:wght@700&display=swap" rel="stylesheet">
<style>
:root{
  --navy:#353d8f;
  --navy-dark:#1a1d40;
  --green:#8cc63f;
  --yellow:#fff200;
  --orange:#f15a24;
  --ink:#333;
  --paper:#f5f4f0;
  --white:#fff;
}
*{margin:0;padding:0;box-sizing:border-box}
html,body{width:957px;height:1200px;overflow:hidden;background:var(--paper)}
.flyer{position:relative;width:957px;height:1200px;background:var(--paper);font-family:"Open Sans",sans-serif;color:var(--ink)}
.hero{position:absolute;left:0;top:0;width:957px;height:574px;
  background:radial-gradient(ellipse 300px 330px at 250px 300px,rgba(200,150,110,.55) 0%,rgba(170,130,80,.25) 45%,rgba(120,170,60,0) 80%),
  linear-gradient(135deg,#6fb33a 0%,#9bd25a 45%,#7cc243 70%,#4e9e28 100%)}
.abs{position:absolute}
.title{right:50px;top:50px;text-align:right;font-family:"PT Sans",sans-serif;font-style:italic;font-weight:700;font-size:47px;line-height:61px;color:var(--white);text-shadow:1px 2px 4px rgba(0,0,0,.35)}
.label{right:50px;font-family:"Montserrat",sans-serif;font-weight:600;font-size:31px;color:var(--yellow);text-align:right}
.info{right:50px;text-align:right;font-family:"PT Sans",sans-serif;font-weight:700;font-size:23px;line-height:31px;color:#111}
.cost{left:718px;top:515px;width:189px;height:40px;background:var(--navy);border-radius:5px;color:var(--white);font-family:"Roboto Condensed",sans-serif;font-weight:700;font-size:27px;line-height:40px;text-align:center}
.tagline{left:120px;width:370px;top:442px;text-align:center;font-family:"PT Sans",sans-serif;font-style:italic;font-weight:700;font-size:19px;line-height:26px;color:var(--white);text-shadow:1px 1px 3px rgba(0,0,0,.5)}
.url-tab{left:71px;top:534px}
.url-tab span{position:absolute;left:0;top:0;width:448px;height:48px;line-height:48px;text-align:center;font-family:"Montserrat",sans-serif;font-weight:600;font-size:28px;color:var(--white);letter-spacing:.5px}
.intro{left:52px;top:606px;width:856px;font-size:13.6px;line-height:21px}
.agenda{left:36px;top:685px}
.agenda span{position:absolute;left:14px;top:6px;font-family:"Montserrat",sans-serif;font-weight:600;font-size:28px;color:var(--white)}
.col{width:473px}
.col-left{left:52px;top:752px}
.col-right{left:579px;top:752px;width:330px}
.time{font-family:"Montserrat",sans-serif;font-weight:600;font-size:18px;color:var(--orange);margin-bottom:8px;line-height:24px}
.time small{font-family:"Open Sans",sans-serif;font-weight:400;font-size:18px;color:var(--ink)}
.item{font-size:13.3px;line-height:18px;margin-bottom:10px;text-align:justify}
.item b{font-style:italic;font-weight:700;font-size:15px}
.divider{left:557px;top:752px;width:1px;height:290px;background:#d5d3cc}
.brand{font-family:"Montserrat",sans-serif;font-weight:600;font-size:38px;color:var(--orange);margin:22px 0 8px}
.link{font-size:13.3px;font-weight:600;line-height:18px;color:var(--navy);word-break:break-all}
.footer{left:0;top:1070px}
.call{right:52px;top:1125px;font-family:"Roboto Condensed",sans-serif;font-weight:700;font-size:27px;color:var(--white)}
.call strong{font-size:38px}
</style>
</head>
<body>
<main class="flyer">
  <div class="hero" role="img" aria-label="Photograph of a laughing woman lying in bright green grass"></div>

  <h1 class="abs title">Fundraising Study Day<br>East of England.<br>Lift the January blues!</h1>

  <h2 class="abs label" style="top:286px">Location</h2>
  <p class="abs info" style="top:324px">Meadowgate Hotel, Orchard Way,<br>Elmford, EF4 2RK</p>

  <h2 class="abs label" style="top:413px">Date And Time</h2>
  <p class="abs info" style="top:450px">Fri 19 January 2018<br>09:00-16:30 GMT</p>
  <div class="abs cost">Cost - £101.48</div>

  <p class="abs tagline">Event of lectures for<br>DENTAL HYGIENISTS and THERAPISTS<br>in support of the exemption campaign.</p>

  <div class="abs url-tab">
    <svg width="448" height="52" viewBox="0 0 448 52"><path d="M4 48 L28 2 H420 L444 48 Z" fill="#353d8f"/><path d="M0 46 H10 L10 52 Z M448 46 H438 L438 52 Z" fill="#1a1d40"/></svg>
    <span>www.ticketbay.co.uk</span>
  </div>

  <p class="abs intro">A fundraising event to support our exemptions project. The day will consist of a series of presentations ranging from the new ECPD to new technologies. The aim, being to enhance our learning and raise funds to support the exemptions campaign. The speaker line includes some of the UK and Irelands most respected dental professionals in our field.</p>

  <div class="abs agenda">
    <svg width="871" height="55" viewBox="0 0 871 55"><rect x="160" y="0" width="711" height="47" fill="#8cc63f"/><path d="M0 0 H197 L170 47 H0 Z" fill="#353d8f"/><path d="M0 47 H8 V55 Z" fill="#1a1d40"/></svg>
    <span>Agenda</span>
  </div>

  <section class="abs col col-left">
    <p class="time">9.30 - 10.15</p>
    <p class="item"><b>Fiona Hartwell:</b> Immediate past president of the ADHT will be updating us on all things ECPD</p>
    <p class="time">10.15 - 11.00</p>
    <p class="item"><b>Megan Fairbrook:</b> Will provide an update on teeth whiteing and explain how social media has impacted her business</p>
    <p class="item"><b>Juliette Raines:</b> Our internationally acclaimed speaker will update our knowledge of periodontal disease and nutrition and new technologies.</p>
    <p class="time">11.00 - 11.30 &nbsp;<small>Break</small></p>
    <p class="time">11.30 - 13.00</p>
    <p class="item"><b>Siobhan Kerrigan &amp; Melanie Pritchard:</b> Will be providing a combined presentation on 'Scaling your business' and start to finish Sonivra techniques. The aim being to build our business with effective communications, systems and protocols. This sessions promises audience participation!</p>
    <p class="time">12 - 1400 <small>lunch</small></p>
  </section>

  <div class="abs divider"></div>

  <section class="abs col col-right">
    <p class="time">14 - 15.00</p>
    <p class="item"><b>Pat Patel:</b> Save your back. All things posture.</p>
    <p class="time">15.00 - 15.30 <small>Break</small></p>
    <p class="time">15.30 16.30</p>
    <p class="item"><b>Juliette Raines:</b> Our internationally acclaimed speaker will update our knowledge of periodontal disease and nutrition and new technologies.</p>
    <p class="brand">Ticketbay</p>
    <p class="link">https://www.ticketbay.co.uk/e/fundraising-study-day-east-of-england-lift-the-january-blues-tickets-48210573316</p>
  </section>

  <svg class="abs footer" width="957" height="130" viewBox="0 0 957 130">
    <path d="M0 130 V100 C250 118 520 20 957 22 V130 Z" fill="#353d8f"/>
    <path d="M0 98 C260 115 520 10 957 18 L957 24 C520 18 250 118 0 102 Z" fill="#8cc63f"/>
    <path d="M0 92 C260 108 520 2 957 12" fill="none" stroke="#f7931e" stroke-width="1.5"/>
  </svg>
  <p class="abs call">Call Us: <strong>000.000.0000</strong></p>
</main>
</body>
</html>
```